i need a business card for a plumbing company in california

we are a drain cleaning , maintenance plumbing company who is starting new marketing campaign for a tatrench-less pipe installation department .

Target Market(s)

the professional who appreciates time and quality workmanship.

Industry/Entity Type

Plumbing

Colors
0655a3
ec1f27

Requirements
Must have
• the second logo needs to be included
Nice to have
• a focus on the services offered
Should not have
• any underlined words on the brief

```html
<!DOCTYPE html>
<html lang="en">
<head>
<meta charset="utf-8">
<title>Clearline Plumbing – Business Card</title>
<link rel="stylesheet" href="https://fonts.googleapis.com/css2?family=Arimo:wght@400;700&display=swap">
<style>
  :root {
    --brand-red: #dd2228;
    --card-white: #f8f8f7;
    --logo-grey: #6e6f6a;
    --text-light: #ffffff;
    --stage: #e8e5e2;
  }
  * { margin: 0; padding: 0; box-sizing: border-box; }
  html, body {
    width: 1200px;
    height: 900px;
    overflow: hidden;
    background: var(--stage);
    font-family: "Arimo", Arial, sans-serif;
  }
  .stage {
    width: 1200px;
    height: 900px;
    display: flex;
    align-items: center;
    justify-content: center;
  }
  .business-card {
    position: relative;
    width: 900px;
    height: 556px;
    background: var(--card-white);
    box-shadow: 0 18px 40px rgba(0,0,0,0.18);
    overflow: hidden;
  }
  .red-panel {
    position: absolute;
    inset: 0;
    width: 100%;
    height: 100%;
  }
  .red-panel polygon { fill: var(--brand-red); }
  .contact-block {
    position: absolute;
    left: 50px;
    top: 148px;
    color: var(--text-light);
  }
  .holder-name {
    font-size: 33px;
    font-weight: 700;
    letter-spacing: 0.3px;
    line-height: 1.1;
  }
  .holder-title {
    font-size: 25px;
    font-weight: 400;
    margin-top: 4px;
  }
  .contact-list {
    list-style: none;
    margin-top: 34px;
  }
  .contact-list li {
    display: flex;
    align-items: center;
    gap: 5px;
    font-size: 25px;
    line-height: 33px;
  }
  .contact-list svg {
    width: 22px;
    height: 22px;
    fill: var(--text-light);
    flex: none;
  }
  .address {
    margin-top: 28px;
    font-size: 25px;
    line-height: 33px;
    font-style: normal;
  }
  .company-name {
    position: absolute;
    left: 498px;
    top: 318px;
    display: flex;
    align-items: center;
    gap: 16px;
  }
  .company-name .wordmark {
    font-size: 48px;
    font-weight: 700;
    line-height: 46px;
    color: var(--logo-grey);
  }
  .company-name .brand-dot {
    width: 40px;
    height: 40px;
    border-radius: 50%;
    background: var(--brand-red);
  }
</style>
</head>
<body>
<main class="stage">
  <article class="business-card">
    <svg class="red-panel" viewBox="0 0 900 556" preserveAspectRatio="none" aria-hidden="true">
      <polygon points="0,0 350,0 510,556 0,556"/>
    </svg>

    <section class="contact-block">
      <h1 class="holder-name">DANIEL REYES</h1>
      <p class="holder-title">Managing Director</p>

      <ul class="contact-list">
        <li>
          <svg viewBox="0 0 24 24" aria-label="Phone"><path d="M3 8c0-2 3-4 9-4s9 2 9 4v2h-5V8.5c-1-.4-2.4-.6-4-.6s-3 .2-4 .6V10H3z"/><path d="M6 11h12l2 8H4z"/></svg>
          021-555 204 318
        </li>
        <li>
          <svg viewBox="0 0 24 24" aria-label="Mobile"><path d="M7 2h10a1 1 0 0 1 1 1v18a1 1 0 0 1-1 1H7a1 1 0 0 1-1-1V3a1 1 0 0 1 1-1zm1 3v13h8V5z"/></svg>
          021-555 204 318
        </li>
        <li>
          <svg viewBox="0 0 24 24" aria-label="Email"><path d="M2 5h20v14H2zm2 2v.5l8 5.5 8-5.5V7l-8 5.3z"/></svg>
          hello@clearlineplumb.com
        </li>
        <li>
          <svg viewBox="0 0 24 24" aria-label="Website"><circle cx="12" cy="12" r="10"/><path d="M8 8c2 0 3 1 2 3s1 3 0 5M15 5c-1 2 1 3 3 3M14 14c2 0 3 1 2 4" stroke="#dd2228" stroke-width="1.6" fill="none"/></svg>
          www.clearlineplumb.com
        </li>
      </ul>

      <address class="address">
        4820 Harbor View Road<br>
        Oakdale, CA 95361
      </address>
    </section>

    <div class="company-name">
      <p class="wordmark">Clearline<br>Plumbing</p>
      <span class="brand-dot" aria-hidden="true"></span>
    </div>
  </article>
</main>
</body>
</html>
```